Social Media Graphics - Bright Ridge Run REVISED

Create 6-7 individual social media graphics (square size) to encourage folks to join our online course called:

The Copper Ladder Plan
How to Launch a Multi-Million Business From Scratch
Sign Up Today!

IMPORTANT: Make the largest and most prominent text on the graphic be: How to Launch a Multi-Million Business From Scratch

For the color scheme of the graphics, let's try a blue color palette; make sure the graphics appeal to both men and women

Make sure each graphic contains 1 of the 3 pics attached (crop pic as needed); and make sure one of the graphics is all TEXT only.

Target Market(s)

men and women looking to start a business

Industry/Entity Type

Entrepreneurship

Colors
0054AA
0677BA
7BADD7
CADEEF
E8F1F8

Requirements
Must have
• All the text and use the 3 pics provided; one graphic can be all text; Simple, modern design that's easy to read

```html
<!DOCTYPE html>
<html lang="en">
<head>
<meta charset="utf-8">
<title>The Copper Ladder Plan – Social Graphic</title>
<link rel="stylesheet" href="https://fonts.googleapis.com/css2?family=Anton&family=Josefin+Sans:wght@400;600&family=Lilita+One&family=Montserrat:wght@600;800&family=Mr+Dafoe&display=swap">
<style>
  :root{
    --blue-deep:#06176a;
    --blue-mid:#0a47c8;
    --blue-bright:#0e63dd;
    --blue-sky:#6fb0f5;
    --blue-pale:#cadeef;
    --blue-mist:#e8f1f8;
    --bar:#4f96ea;
    --gold:#ffd21a;
    --gold-deep:#f4a40a;
    --orange:#f58a1f;
    --white:#ffffff;
  }
  *{margin:0;padding:0;box-sizing:border-box}
  html,body{width:1200px;height:1176px;overflow:hidden;background:var(--blue-deep)}
  .graphic{
    position:relative;width:1200px;height:1176px;overflow:hidden;
    background:
      radial-gradient(ellipse at 45% 28%, var(--blue-bright) 0%, rgba(14,99,221,0) 55%),
      linear-gradient(180deg, var(--blue-mid) 0%, #0938b4 45%, #081f86 78%, var(--blue-deep) 100%);
    font-family:"Montserrat",sans-serif;
  }
  .backdrop-word{
    position:absolute;left:10px;top:-28px;white-space:nowrap;
    font-family:"Josefin Sans",sans-serif;font-weight:600;font-size:190px;
    color:rgba(6,30,120,.35);letter-spacing:4px;
  }
  .art{position:absolute}
  .art-bills{left:0;top:0;width:170px;height:770px;
    background:linear-gradient(180deg,rgba(190,200,170,.25),rgba(120,140,120,.12) 60%,rgba(120,140,120,0));}
  .art-coins{left:1100px;top:0;width:100px;height:480px;
    background:linear-gradient(180deg,rgba(240,170,50,.35),rgba(240,170,50,.1) 70%,rgba(240,170,50,0));}
  .art-rocket{left:770px;top:242px;width:280px;height:222px;border-radius:40px;
    background:radial-gradient(ellipse,rgba(80,170,255,.75),rgba(60,140,240,0) 70%);}
  .art-hosts{left:258px;top:220px;width:690px;height:600px;border-radius:12px 12px 0 0;
    background:linear-gradient(90deg,#c2366f 0%,#b43a7a 40%,#1a1c2e 55%,#101424 100%);
    -webkit-mask:linear-gradient(180deg,#000 80%,transparent 100%);
            mask:linear-gradient(180deg,#000 80%,transparent 100%);}
  .chart{position:absolute;left:0;top:0;width:1200px;height:840px}
  .title{position:absolute;left:280px;top:56px;height:170px;width:700px;color:var(--white)}
  .title-big{position:absolute;left:0;top:0;font-family:"Anton",sans-serif;font-size:165px;line-height:1;
    transform:scaleX(.75);transform-origin:left top}
  .title-top{position:absolute;left:178px;top:14px;font-family:"Josefin Sans",sans-serif;font-weight:400;font-size:60px;line-height:1;white-space:nowrap}
  .title-box{position:absolute;left:178px;top:87px;width:521px;height:67px;border:2px solid var(--blue-sky);
    display:flex;align-items:center;justify-content:center;
    font-family:"Josefin Sans",sans-serif;font-size:44px;letter-spacing:10px;white-space:nowrap;padding-top:6px}
  .headline{position:absolute;left:0;width:1200px;text-align:center;white-space:nowrap;font-family:"Lilita One",sans-serif;line-height:1}
  .headline-top{top:770px;left:2px;font-size:104px;color:var(--gold);
    text-shadow:3px 4px 0 var(--gold-deep),5px 6px 0 #2f7cf0}
  .headline-main{top:868px;left:2px;font-size:89px;color:var(--white);
    text-shadow:3px 4px 0 var(--orange),5px 6px 0 #c9560e}
  .from{position:absolute;left:331px;top:968px;font-family:"Mr Dafoe",cursive;font-size:60px;line-height:1;color:var(--white)}
  .scratch{position:absolute;left:461px;top:950px;font-family:"Josefin Sans",sans-serif;font-weight:400;font-size:90px;color:var(--blue-sky);line-height:1;white-space:nowrap}
  .cta{position:absolute;left:381px;top:1054px;width:438px;height:51px;border-radius:26px;
    background:linear-gradient(90deg,#1f6ff2,#5ca5f6);
    display:flex;align-items:center;justify-content:center;
    color:var(--white);font-size:29px;font-weight:600;letter-spacing:4px}
  .cta strong{font-weight:800;margin-left:12px}
</style>
</head>
<body>
<main class="graphic">
  <div class="backdrop-word" aria-hidden="true">MULTI-MILLION</div>

  <svg class="chart" viewBox="0 0 1200 840" aria-hidden="true">
    <rect x="959" y="463" width="34" height="377" fill="var(--bar)" opacity=".75"/>
    <rect x="1031" y="379" width="34" height="461" fill="var(--bar)" opacity=".8"/>
    <rect x="1104" y="314" width="34" height="526" fill="var(--bar)" opacity=".85"/>
    <rect x="1174" y="274" width="26" height="566" fill="var(--bar)" opacity=".9"/>
  </svg>

  <div class="art art-bills" role="img" aria-label="Falling dollar bills"></div>
  <div class="art art-coins" role="img" aria-label="Falling gold coins"></div>
  <div class="art art-rocket" role="img" aria-label="Glowing blue rocket illustration"></div>
  <div class="art art-hosts" role="img" aria-label="Photo of the two course hosts smiling"></div>

  <header class="title">
    <span class="title-big">THE</span>
    <span class="title-top">COPPER</span>
    <span class="title-box">LADDER PLAN</span>
  </header>

  <h1>
    <span class="headline headline-top">HOW TO LAUNCH A</span>
    <span class="headline headline-main">MULTI-MILLION BUSINESS</span>
    <span class="from">From</span>
    <span class="scratch">SCRATCH</span>
  </h1>

  <div class="cta">SIGN UP<strong>TODAY!</strong></div>
</main>
</body>
</html>
```